Restaurant Email Club Sign Up Poster

Looking for a creative design that will catch people's eye and prompt them to sign up for our email club for our Restaurant that we run in Omaha, Nebraska. Open to any creative ways to most effectively grab peoples attention quickly without being too confusing. Want it to be simple but actionable.

Have attached some documents for your assistance - in addition to some marketing materials we have put out in the past.

Would like to put design on posters to hang up throughout the restaurant and likely will make stickers to put on check presenters as well.

Catchy stock photo or use of the cheese curd photo probably good idea - callout things mentioned in the "must haves" section below. Looking for most creative and catchy, yet simple design.

Target Market(s)

30-50 year olds males and females.

Industry/Entity Type

Restaurant

Requirements
Must have
• Must include callouts for -
• Sign up for E-Club for access to future offers and events (or something along these lines)
• Free Appetizer for Signing Up
• Free Birthday Meal
Should not have
• Please do not make this poster like the postcard that I attached to the project - this is not a poster to call out that we are a new burger and beer spot, that we have 40 rotating taps, or that we have 15 specialty burgers, etc. This is simply a poster to grab someones attention and get them to sign up for our email club. Should maybe have a catchy question, something like, "Want a Free Appetizer?" or something catchy and similar, and then below say "And access to future deals and event happenings?"

```html
<!DOCTYPE html>
<html lang="en">
<head>
<meta charset="utf-8">
<title>E-Club Sign Up Poster</title>
<link rel="stylesheet" href="https://fonts.googleapis.com/css2?family=Bungee&family=Roboto+Condensed:wght@700&display=swap">
<style>
  :root {
    --paper: #e6e6e6;
    --red: #c4121a;
    --ink: #111111;
    --glow-outer: #f08a12;
    --glow-mid: #ffc21f;
    --glow-inner: #ffffff;
    --btn-top: #ffe14a;
    --btn-bottom: #f6a91b;
    --curd-light: #e9a54a;
    --curd-dark: #a2521c;
  }
  * { margin: 0; padding: 0; box-sizing: border-box; }
  html, body { width: 849px; height: 1200px; overflow: hidden; background: var(--paper); }
  .poster { position: relative; width: 849px; height: 1200px; background: var(--paper); overflow: hidden; }

  .brand { position: absolute; left: 34px; top: 50px; display: flex; align-items: center; gap: 10px; z-index: 2; }
  .brand-dot { width: 26px; height: 26px; border-radius: 50%; background: var(--ink); }
  .brand-name { font-family: "Roboto Condensed", sans-serif; font-weight: 700; font-size: 22px; color: var(--ink); letter-spacing: 1px; text-transform: uppercase; }

  .glow-area {
    position: absolute; left: 121px; top: 50px; width: 656px; height: 620px;
    border-radius: 50%;
    background: radial-gradient(ellipse at center, var(--glow-inner) 0%, var(--glow-inner) 55%, var(--glow-mid) 80%, var(--glow-outer) 100%);
  }

  .food-photo {
    position: absolute; left: 185px; top: 270px; width: 470px; height: 260px;
    border-radius: 40px 60px 30px 50px;
    background: radial-gradient(ellipse at 45% 40%, var(--curd-light) 0%, #c97a32 55%, var(--curd-dark) 100%);
  }

  .headline {
    position: absolute; left: 40px; top: 470px; width: 760px;
    transform: rotate(-7deg); transform-origin: center;
    text-align: center;
  }
  .headline-question {
    font-family: "Bungee", sans-serif; font-size: 86px; line-height: 0.98; font-weight: 400;
    color: var(--red); -webkit-text-stroke: 2px #fff;
    text-shadow: 4px 6px 0 rgba(0,0,0,0.45);
  }
  .headline-sub {
    margin-top: 14px; font-family: "Bungee", sans-serif; font-size: 35px; line-height: 1.15;
    color: var(--red); text-shadow: 2px 3px 0 rgba(0,0,0,0.2);
  }

  .perk { position: absolute; left: 0; width: 849px; height: 110px; }
  .perk-box {
    position: absolute; left: 172px; width: 534px; height: 100%;
    display: flex; align-items: center; justify-content: center; text-align: center;
    border-radius: 14px 14px 0 0;
    background: linear-gradient(180deg, var(--btn-top), var(--btn-bottom));
    font-family: "Roboto Condensed", sans-serif; font-weight: 700; color: var(--ink);
    font-size: 28px; line-height: 1.3; text-transform: uppercase;
  }
  .perk-box.is-large { font-size: 37px; }
  .chevron { position: absolute; top: 50%; width: 60px; height: 44px; margin-top: -22px; }
  .chevron-left { left: 88px; }
  .chevron-right { left: 726px; }
  .perk-eclub { top: 772px; }
  .perk-appetizer { top: 900px; }
  .perk-birthday { top: 1029px; }
</style>
</head>
<body>
<main class="poster">
  <div class="brand">
    <span class="brand-dot"></span>
    <span class="brand-name">Ironhorn Tap</span>
  </div>

  <div class="glow-area" role="img" aria-label="Orange and yellow starburst behind the food photo"></div>

  <div class="food-photo" role="img" aria-label="Photo of golden fried cheese curds"></div>

  <header class="headline">
    <h1 class="headline-question">Want a free<br>appetizer?</h1>
    <p class="headline-sub">And access to future deals<br>and event happenings?</p>
  </header>

  <section class="perk perk-eclub">
    <svg class="chevron chevron-left" viewBox="0 0 60 44" aria-hidden="true"><polygon fill="var(--red)" points="0,0 12,0 28,22 12,44 0,44 16,22"/><polygon fill="var(--red)" points="26,0 38,0 54,22 38,44 26,44 42,22"/></svg>
    <div class="perk-box">Sign up for e-club for access<br>to future offers and events</div>
    <svg class="chevron chevron-right" viewBox="0 0 60 44" aria-hidden="true"><polygon fill="var(--red)" points="60,0 48,0 32,22 48,44 60,44 44,22"/><polygon fill="var(--red)" points="34,0 22,0 6,22 22,44 34,44 18,22"/></svg>
  </section>

  <section class="perk perk-appetizer">
    <svg class="chevron chevron-left" viewBox="0 0 60 44" aria-hidden="true"><polygon fill="var(--red)" points="0,0 12,0 28,22 12,44 0,44 16,22"/><polygon fill="var(--red)" points="26,0 38,0 54,22 38,44 26,44 42,22"/></svg>
    <div class="perk-box">Free appetizer for signing up</div>
    <svg class="chevron chevron-right" viewBox="0 0 60 44" aria-hidden="true"><polygon fill="var(--red)" points="60,0 48,0 32,22 48,44 60,44 44,22"/><polygon fill="var(--red)" points="34,0 22,0 6,22 22,44 34,44 18,22"/></svg>
  </section>

  <section class="perk perk-birthday">
    <svg class="chevron chevron-left" viewBox="0 0 60 44" aria-hidden="true"><polygon fill="var(--red)" points="0,0 12,0 28,22 12,44 0,44 16,22"/><polygon fill="var(--red)" points="26,0 38,0 54,22 38,44 26,44 42,22"/></svg>
    <div class="perk-box is-large">Free birthday meal</div>
    <svg class="chevron chevron-right" viewBox="0 0 60 44" aria-hidden="true"><polygon fill="var(--red)" points="60,0 48,0 32,22 48,44 60,44 44,22"/><polygon fill="var(--red)" points="34,0 22,0 6,22 22,44 34,44 18,22"/></svg>
  </section>
</main>
</body>
</html>
```